Adventure Business Cards

Please check out our website for style
Vertical card
Details:
Side 1
Logo
Business name: Kestrel Bay Wildlife Tours
Name: Colin Marsby
Role: Director
Email: info@kestrelbaywildtours.example
Address: PO Box 71, Fennick Point NSW 2741
Phone: +61 2 5550 4817
Web address: www.kestrelbaywildtours.example
Side 2
Taking pictures?
A Facebook and Instagram logo
Tag us in your pictures with
#kbwildtoursco
@kbwildtoursco
www.kestrelbaywildtours.example
Details:
Side 1
Logo
Name: Colin Marsby
Role: Director
Phone: +61 2 5550 4817
Side 2
Taking pictures?
#kbwildtoursco
@kbwildtoursco

```html
<!DOCTYPE html>
<html lang="en">
<head>
<meta charset="utf-8">
<title>Kestrel Bay Wildlife Tours – Business Cards</title>
<link rel="stylesheet" href="https://fonts.googleapis.com/css2?family=Open+Sans:wght@400;700&display=swap">
<style>
  :root {
    --page: #d9d9d9;
    --card-black: #0d0d0d;
    --card-black-edge: #1c1c1c;
    --teal-light: #2a7f96;
    --teal-mid: #155a70;
    --teal-dark: #062635;
    --accent-blue: #3a9bd5;
    --text-white: #f2f2f2;
    --text-soft: #d6dde2;
    --mark-fill: #10202a;
    --divider: rgba(255,255,255,0.35);
  }
  * { box-sizing: border-box; margin: 0; padding: 0; }
  html, body { width: 1200px; height: 900px; overflow: hidden; }
  body {
    background: var(--page);
    font-family: "Open Sans", Arial, sans-serif;
    display: flex;
    align-items: center;
    justify-content: center;
    gap: 80px;
  }
  .card {
    width: 340px;
    height: 590px;
    border-radius: 4px;
    position: relative;
    overflow: hidden;
    box-shadow: 0 6px 18px rgba(0,0,0,0.25);
    display: flex;
    flex-direction: column;
    align-items: center;
  }
  .brand-mark {
    border-radius: 50%;
    background: var(--mark-fill);
    display: flex;
    align-items: center;
    justify-content: center;
    text-align: center;
    color: var(--text-white);
    font-weight: 700;
    line-height: 1.25;
    flex-shrink: 0;
  }

  /* Front side */
  .card--front {
    background: radial-gradient(ellipse at 40% 35%, var(--card-black-edge) 0%, var(--card-black) 75%);
    color: var(--text-white);
  }
  .card--front .brand-mark {
    width: 170px; height: 170px;
    margin-top: 52px;
    font-size: 17px;
    padding: 0 20px;
  }
  .details {
    align-self: stretch;
    padding: 44px 34px 0;
  }
  .person-name { color: var(--accent-blue); font-weight: 700; font-size: 18px; }
  .person-role { font-size: 12.5px; margin-top: 2px; }
  .contact-list { list-style: none; margin-top: 22px; font-size: 13px; color: var(--text-soft); }
  .contact-list li { display: flex; align-items: center; gap: 8px; line-height: 1.6; white-space: nowrap; }
  .contact-list svg { width: 11px; height: 11px; fill: var(--accent-blue); flex-shrink: 0; }
  .company-name { margin-top: 18px; color: var(--accent-blue); font-weight: 700; font-size: 14.5px; }
  .company-address { font-size: 13px; color: var(--text-soft); }
  .company-web { margin-top: 14px; color: var(--accent-blue); font-weight: 700; font-size: 14px; white-space: nowrap; }

  /* Back side */
  .card--back {
    background: radial-gradient(ellipse at 50% 30%, var(--teal-light) 0%, var(--teal-mid) 45%, var(--teal-dark) 100%);
    color: var(--text-white);
    text-align: center;
  }
  .card--back .brand-mark {
    width: 150px; height: 150px;
    margin-top: 56px;
    font-size: 15px;
    padding: 0 18px;
  }
  .tag-heading { margin-top: 40px; font-size: 20px; font-weight: 700; }
  .tag-lead { margin-top: 6px; font-size: 13px; color: var(--text-soft); }
  .social-list {
    list-style: none;
    margin-top: 26px;
    width: 240px;
    font-size: 13.5px;
  }
  .social-item {
    display: flex;
    flex-direction: column;
    align-items: center;
    gap: 6px;
    padding: 12px 0;
    white-space: nowrap;
  }
  .social-item + .social-item { border-top: 1px solid var(--divider); }
  .icon-square { width: 22px; height: 22px; border: 2px solid var(--text-white); border-radius: 5px; }
  .icon-circle { width: 22px; height: 22px; border: 2px solid var(--text-white); border-radius: 50%; }
</style>
</head>
<body>

  <section class="card card--front" aria-label="Business card side 1">
    <div class="brand-mark">Kestrel Bay Wildlife Tours</div>
    <div class="details">
      <p class="person-name">Colin Marsby</p>
      <p class="person-role">Director</p>
      <ul class="contact-list">
        <li>
          <svg viewBox="0 0 24 24" aria-hidden="true"><path d="M6.6 10.8a15 15 0 0 0 6.6 6.6l2.2-2.2a1 1 0 0 1 1-.25 11.4 11.4 0 0 0 3.6.57 1 1 0 0 1 1 1V20a1 1 0 0 1-1 1A17 17 0 0 1 3 4a1 1 0 0 1 1-1h3.5a1 1 0 0 1 1 1c0 1.25.2 2.45.57 3.57a1 1 0 0 1-.25 1z"/></svg>
          +61 2 5550 4817
        </li>
        <li>
          <svg viewBox="0 0 24 24" aria-hidden="true"><path d="M2 5h20v14H2z M2 5l10 8 10-8"/></svg>
          info@kestrelbaywildtours.example
        </li>
      </ul>
      <p class="company-name">Kestrel Bay Wildlife Tours</p>
      <p class="company-address">PO Box 71, Fennick Point NSW 2741</p>
      <p class="company-web">www.kestrelbaywildtours.example</p>
    </div>
  </section>

  <section class="card card--back" aria-label="Business card side 2">
    <div class="brand-mark">Kestrel Bay Wildlife Tours</div>
    <p class="tag-heading">Taking pictures?</p>
    <p class="tag-lead">Tag us in your pictures with</p>
    <ul class="social-list">
      <li class="social-item">
        <span class="icon-circle" aria-hidden="true"></span>
        <span>#kbwildtoursco</span>
      </li>
      <li class="social-item">
        <span class="icon-square" aria-hidden="true"></span>
        <span>@kbwildtoursco</span>
      </li>
      <li class="social-item">
        <svg width="22" height="22" viewBox="0 0 24 24" fill="none" stroke="#f2f2f2" stroke-width="1.6" aria-hidden="true">
          <circle cx="12" cy="12" r="10"/>
          <ellipse cx="12" cy="12" rx="4.5" ry="10"/>
          <line x1="2" y1="12" x2="22" y2="12"/>
          <line x1="4" y1="7" x2="20" y2="7"/>
          <line x1="4" y1="17" x2="20" y2="17"/>
        </svg>
        <span>www.kestrelbaywildtours.example</span>
      </li>
    </ul>
  </section>

</body>
</html>
```